Billboard

we want our Hop & Skip logo really big, we need this to stand out

Use a really bold font for the wording as it's on a billboard on the highway

Hop & Skip Logo
perhaps on left hand side really large then have a slanting line and a different colour background for the other side.

Wording BELOW-bold

TOUR NOW

hopandskip.edu.au

Use one image,
I have attached other designs we have been using for our campaign so a similar look would be great.
specs- 1224 W × 324 H px JPEG

Target Market(s)
families

Industry/Entity Type
childcare

Target Market(s)

families

Industry/Entity Type

childcare

Requirements
Must have
• bold font and big logo

```html
<!DOCTYPE html>
<html lang="en">
<head>
<meta charset="utf-8">
<title>Hop &amp; Skip — Tour Now Billboard</title>
<link rel="stylesheet" href="https://fonts.googleapis.com/css2?family=Bebas+Neue&family=Poppins:wght@500;600;800&display=swap">
<style>
  :root {
    --stage: #333333;
    --sky-blue: #0aa0ef;
    --sunny-yellow: #fbf304;
    --white: #ffffff;
    --ink: #111111;
    --photo-warm: #c9864f;
    --photo-deep: #5a3a24;
    --photo-teal: #2a8fb0;
  }
  * { margin: 0; padding: 0; box-sizing: border-box; }
  html, body {
    width: 1200px;
    height: 1200px;
    overflow: hidden;
    background: var(--stage);
  }
  .billboard {
    position: absolute;
    left: 50px;
    top: 454px;
    width: 1100px;
    height: 292px;
    background: var(--sky-blue);
    overflow: hidden;
    box-shadow: 0 14px 30px rgba(0, 0, 0, 0.45);
  }
  .billboard__art {
    position: absolute;
    inset: 0;
    width: 1100px;
    height: 292px;
  }
  .brand {
    position: absolute;
    left: 22px;
    top: 0;
    width: 190px;
    height: 292px;
    display: flex;
    flex-direction: column;
    align-items: center;
    justify-content: center;
    gap: 14px;
  }
  .brand__dot {
    width: 78px;
    height: 78px;
    border-radius: 50%;
    background: var(--sunny-yellow);
  }
  .brand__name {
    font-family: "Poppins", sans-serif;
    font-weight: 800;
    font-size: 33px;
    line-height: 1;
    color: var(--white);
    white-space: nowrap;
    letter-spacing: -0.5px;
  }
  .headline {
    position: absolute;
    left: 790px;
    top: 22px;
    width: 270px;
    text-align: center;
  }
  .headline__tour {
    display: block;
    font-family: "Bebas Neue", "Oswald", sans-serif;
    font-size: 158px;
    line-height: 0.82;
    color: var(--sunny-yellow);
    letter-spacing: 1px;
  }
  .headline__now {
    display: block;
    margin-top: 8px;
    font-family: "Poppins", sans-serif;
    font-weight: 600;
    font-size: 80px;
    line-height: 0.9;
    color: var(--white);
    letter-spacing: -1px;
  }
  .web-link {
    position: absolute;
    left: 770px;
    top: 237px;
    height: 55px;
    display: flex;
    align-items: center;
    gap: 10px;
    font-family: "Poppins", sans-serif;
    font-weight: 500;
    font-size: 26px;
    color: var(--ink);
  }
  .web-link__icon { width: 28px; height: 28px; flex: none; }
</style>
</head>
<body>
  <main class="billboard">
    <svg class="billboard__art" viewBox="0 0 1100 292" xmlns="http://www.w3.org/2000/svg">
      <defs>
        <linearGradient id="photo-tones" x1="0" y1="0" x2="1" y2="1">
          <stop offset="0" stop-color="var(--photo-deep)"/>
          <stop offset="0.45" stop-color="var(--photo-warm)"/>
          <stop offset="0.75" stop-color="var(--photo-teal)"/>
          <stop offset="1" stop-color="var(--photo-deep)"/>
        </linearGradient>
      </defs>

      <!-- accent shapes behind the photo frame -->
      <path class="accent-shape accent-shape--lower" d="M230 292 L330 150 L430 292 Z" fill="var(--sunny-yellow)" stroke="var(--sunny-yellow)" stroke-width="18" stroke-linejoin="round"/>
      <path class="accent-shape accent-shape--upper" d="M570 -10 L712 -10 L700 40 L630 110 L560 40 Z" fill="var(--sunny-yellow)" stroke="var(--sunny-yellow)" stroke-width="18" stroke-linejoin="round"/>

      <!-- speed lines -->
      <g class="speed-lines" stroke-linecap="round" stroke-width="4">
        <line x1="243" y1="66" x2="313" y2="5" stroke="var(--white)"/>
        <line x1="235" y1="102" x2="339" y2="5" stroke="var(--sunny-yellow)"/>
        <line x1="628" y1="281" x2="703" y2="216" stroke="var(--sunny-yellow)"/>
        <line x1="658" y1="292" x2="703" y2="252" stroke="var(--white)"/>
      </g>

      <!-- photo frame -->
      <rect class="photo-frame" x="303" y="-23" width="348" height="348" rx="34" transform="rotate(45 477 151)" fill="var(--white)"/>
      <rect class="photo" role="img" aria-label="Photo of young children in sun hats playing with buckets and spades in a sandpit" x="317" y="-9" width="320" height="320" rx="26" transform="rotate(45 477 151)" fill="url(#photo-tones)"/>

      <!-- web address band -->
      <path class="link-band" d="M736 237 L1100 237 L1100 292 L700 292 Z" fill="var(--sunny-yellow)"/>
    </svg>

    <div class="brand">
      <span class="brand__dot"></span>
      <span class="brand__name">Hop &amp; Skip</span>
    </div>

    <h1 class="headline">
      <span class="headline__tour">TOUR</span>
      <span class="headline__now">NOW</span>
    </h1>

    <p class="web-link">
      <svg class="web-link__icon" viewBox="0 0 28 28" xmlns="http://www.w3.org/2000/svg" aria-hidden="true">
        <circle cx="14" cy="14" r="14" fill="var(--ink)"/>
        <g fill="none" stroke="var(--white)" stroke-width="1.6">
          <circle cx="14" cy="14" r="8"/>
          <ellipse cx="14" cy="14" rx="3.5" ry="8"/>
          <line x1="6" y1="14" x2="22" y2="14"/>
          <line x1="7.5" y1="10" x2="20.5" y2="10"/>
          <line x1="7.5" y1="18" x2="20.5" y2="18"/>
        </g>
      </svg>
      hopandskip.edu.au
    </p>
  </main>
</body>
</html>
```